sydney wedding photography business needs a business card design

we need a business card design for a sydney based wedding photography and videography business. our business name is :golden hour photography and video. our target clients are 24-35 yrs female. our style is candid, organic, natural, dynamic. we are a team of young photographers and videographers, and help brides to create memories that they will cherish for the rest of their lives. the logo will be provided. we want an elegant design that reflects our style, and also want to give a great impression to our clients that we are one of the best studios in sydney and our brand means quality and premium service.

Target Market(s)

bride to be, 24-35 years old, living in sydney and surrunding areas

Industry/Entity Type

Wedding Photography

Contact Information for Business Card

address: 57 marrow lane, bexton nsw 2041
mobile: 0431872056
phone: (02) 9361 2748
info@goldenhourstudio.net.au
www.goldenhourstudio.net.au
facebook:goldenhourbridals
instagram:goldenhourbridals

Font styles to use
Serif
Sans Serif

Requirements
Nice to have
• maybe add my slogan"memories beyond eternity" if the layout looks good
Should not have
• no black color, not good idea for wedding biz card

```html
<!DOCTYPE html>
<html lang="en">
<head>
<meta charset="utf-8">
<title>Golden Hour Photography and Video – Business Card</title>
<link href="https://fonts.googleapis.com/css2?family=Montserrat:wght@300;400;500&display=swap" rel="stylesheet">
<style>
  :root {
    --gold: #d9a80f;
    --gold-deep: #c08d0a;
    --gold-soft: #f3e6bf;
    --ink: #3a3226;
    --paper: #ffffff;
    --back-light: #f4f4f4;
    --back-dark: #dcdcdc;
    --stage: #ece7de;
  }
  * { box-sizing: border-box; margin: 0; padding: 0; }
  html, body { width: 1200px; height: 1023px; overflow: hidden; }
  body {
    background: var(--stage);
    font-family: "Montserrat", sans-serif;
    color: var(--ink);
    display: flex;
    flex-direction: column;
    align-items: center;
    justify-content: center;
    gap: 60px;
  }
  .card {
    position: relative;
    width: 700px;
    height: 400px;
    border-radius: 18px;
    box-shadow: 0 4px 14px rgba(80, 60, 30, 0.18);
    overflow: hidden;
  }

  /* Front */
  .card-front { background: var(--paper); }
  .front-frame {
    position: absolute;
    inset: 26px;
    border: 2px solid var(--gold);
  }
  .front-logo {
    position: absolute;
    left: 52px;
    top: 14px;
    height: 26px;
    background: var(--paper);
    padding: 0 12px;
    display: flex;
    align-items: center;
    gap: 12px;
  }
  .logo-mark {
    width: 14px; height: 14px;
    border-radius: 50%;
    background: var(--gold);
  }
  .logo-name {
    font-weight: 500;
    color: var(--gold);
    letter-spacing: 3px;
    text-transform: uppercase;
    white-space: nowrap;
  }
  .front-logo .logo-name { font-size: 18px; }
  .front-accent {
    position: absolute;
    right: 72px;
    top: 66px;
    width: 180px;
    height: 180px;
    border-radius: 50%;
    background: radial-gradient(circle, #fbf4df 0%, var(--gold-soft) 100%);
    opacity: 0.75;
  }
  .contact-list {
    position: absolute;
    left: 62px;
    bottom: 70px;
    list-style: none;
    display: flex;
    flex-direction: column;
    gap: 10px;
  }
  .contact-item {
    display: flex;
    align-items: center;
    gap: 12px;
    font-size: 15px;
    font-weight: 400;
    letter-spacing: 0.5px;
  }
  .contact-icon {
    width: 26px; height: 26px;
    border-radius: 4px;
    background: var(--gold-deep);
    display: flex; align-items: center; justify-content: center;
    flex-shrink: 0;
  }
  .contact-icon svg { width: 15px; height: 15px; }
  .front-web {
    position: absolute;
    right: 70px;
    bottom: 16px;
    background: var(--paper);
    padding: 0 10px;
    font-size: 15px;
    color: var(--gold);
    letter-spacing: 0.6px;
  }

  /* Back */
  .card-back {
    background: linear-gradient(135deg, var(--back-dark) 0%, var(--back-light) 45%, #fafafa 70%, var(--back-dark) 100%);
  }
  .back-logo {
    position: absolute;
    inset: 0;
    display: flex;
    align-items: center;
    justify-content: center;
    gap: 14px;
  }
  .back-logo .logo-name { font-size: 28px; letter-spacing: 5px; }
  .back-logo .logo-mark { width: 18px; height: 18px; }
  .social {
    position: absolute;
    left: 36px;
    display: flex;
    align-items: center;
    gap: 10px;
    font-size: 14px;
    letter-spacing: 0.6px;
  }
  .social-top { top: 32px; }
  .social-bottom { bottom: 32px; }
  .social-badge {
    width: 20px; height: 20px;
    border-radius: 3px;
    background: var(--gold-deep);
  }
</style>
</head>
<body>

<section class="card card-front" aria-label="Business card front">
  <div class="front-frame"></div>
  <div class="front-accent" role="img" aria-label="Faint gold ring with gem decoration"></div>
  <div class="front-logo">
    <span class="logo-mark"></span>
    <span class="logo-name">golden hour photography and video</span>
  </div>

  <ul class="contact-list">
    <li class="contact-item">
      <span class="contact-icon">
        <svg viewBox="0 0 24 24" fill="#fff"><path d="M6.6 10.8a15.2 15.2 0 0 0 6.6 6.6l2.2-2.2a1 1 0 0 1 1-.25 11.4 11.4 0 0 0 3.6.57 1 1 0 0 1 1 1V20a1 1 0 0 1-1 1A17 17 0 0 1 3 4a1 1 0 0 1 1-1h3.5a1 1 0 0 1 1 1c0 1.25.2 2.45.57 3.57a1 1 0 0 1-.25 1z"/></svg>
      </span>
      0431872056
    </li>
    <li class="contact-item">
      <span class="contact-icon">
        <svg viewBox="0 0 24 24" fill="none" stroke="#fff" stroke-width="2"><rect x="4" y="6" width="16" height="12" rx="1"/><path d="M8 10h8M8 14h5"/></svg>
      </span>
      (02) 9361 2748
    </li>
    <li class="contact-item">
      <span class="contact-icon">
        <svg viewBox="0 0 24 24" fill="none" stroke="#fff" stroke-width="2"><rect x="3" y="6" width="18" height="12" rx="1"/><path d="M3 7l9 6 9-6"/></svg>
      </span>
      info@goldenhourstudio.net.au
    </li>
    <li class="contact-item">
      <span class="contact-icon">
        <svg viewBox="0 0 24 24" fill="#fff"><path d="M12 2a7 7 0 0 0-7 7c0 5 7 13 7 13s7-8 7-13a7 7 0 0 0-7-7zm0 9.5A2.5 2.5 0 1 1 12 6.5a2.5 2.5 0 0 1 0 5z"/></svg>
      </span>
      57 marrow lane, bexton nsw 2041
    </li>
  </ul>

  <div class="front-web">www.goldenhourstudio.net.au</div>
</section>

<section class="card card-back" aria-label="Business card back">
  <div class="social social-top">
    <span class="social-badge"></span>
    goldenhourbridals
  </div>
  <div class="back-logo">
    <span class="logo-mark"></span>
    <span class="logo-name">golden hour photography</span>
  </div>
  <div class="social social-bottom">
    <span class="social-badge"></span>
    goldenhourbridals
  </div>
</section>

</body>
</html>
```